business cards foreign exchange student company
Bluebird Hosting
Bright & Fun-filled
Mack Dorran
Service Director
Western Region
mack@mybluebirdhosting.com
mybluebirdhosting.com
This business card needs to be unforgettable! It needs to stand out from all the other business cards. Something clever/funny. It needs to communicate this is fun!! this is exciting!! and our theme for our company is "The Best Time Ever!" so the business card should convey that they have just found The Best Time Ever!!!
This will be my new website (with the old logo)
this is a marketing piece used to send families to the website
another marketing piece to get families to the website
This is my logo .ai file
This is my .ai logo file for dark backgrounds

```html
<!DOCTYPE html>
<html lang="en">
<head>
<meta charset="utf-8">
<title>Bluebird Hosting – Business Card</title>
<link rel="stylesheet" href="https://fonts.googleapis.com/css2?family=EB+Garamond:wght@500&display=swap">
<style>
  :root {
    --page-bg: #e9e6e1;
    --card-bg: #ffffff;
    --brand-blue: #1b5f8e;
    --band-dark: #17557f;
    --band-light: #2a78ad;
    --accent-green: #6cb33f;
    --band-text: #d6e8f4;
    --ink: #2f5d80;
    --icon-bg: #1b5f8e;
  }
  * { box-sizing: border-box; margin: 0; padding: 0; }
  html, body { width: 1200px; height: 914px; overflow: hidden; }
  body {
    background: var(--page-bg);
    font-family: "EB Garamond", Georgia, serif;
    font-weight: 500;
    display: flex;
    align-items: center;
    justify-content: center;
  }
  .business-card {
    position: relative;
    width: 1040px;
    height: 594px;
    background: var(--card-bg);
    box-shadow: 0 10px 30px rgba(0,0,0,0.18);
  }
  .brand {
    position: absolute;
    left: 0; right: 0;
    top: 118px;
    display: flex;
    align-items: center;
    justify-content: center;
    gap: 20px;
  }
  .brand-dot {
    width: 74px; height: 74px;
    border-radius: 50%;
    background: var(--brand-blue);
  }
  .brand-text { display: flex; flex-direction: column; }
  .brand-name {
    color: var(--brand-blue);
    font-size: 58px;
    line-height: 1;
  }
  .brand-tagline {
    color: var(--brand-blue);
    font-size: 22px;
    align-self: flex-end;
    margin-top: 4px;
  }
  .name-band {
    position: absolute;
    left: 0; right: 0;
    top: 282px;
    height: 90px;
    background: linear-gradient(180deg, var(--band-light), var(--band-dark));
    border-top: 5px solid var(--accent-green);
    border-bottom: 5px solid var(--accent-green);
    box-shadow: 0 -9px 0 -4px var(--card-bg), 0 -11px 0 -4px var(--accent-green),
                0 9px 0 -4px var(--card-bg), 0 11px 0 -4px var(--accent-green);
    display: flex;
    align-items: center;
    justify-content: center;
  }
  .person {
    color: var(--band-text);
    font-size: 30px;
    font-variant: small-caps;
    letter-spacing: 1.5px;
  }
  .person .divider { margin: 0 10px; }
  .contact {
    position: absolute;
    left: 96px;
    top: 408px;
    color: var(--ink);
    font-size: 19px;
    font-variant: small-caps;
  }
  .contact-row {
    display: flex;
    align-items: center;
    gap: 22px;
    margin-bottom: 14px;
  }
  .contact-item { display: flex; align-items: center; gap: 7px; }
  .icon {
    width: 20px; height: 20px;
    border-radius: 50%;
    background: var(--icon-bg);
    display: inline-flex;
    align-items: center;
    justify-content: center;
  }
  .icon svg { width: 12px; height: 12px; fill: #fff; }
</style>
</head>
<body>
  <main class="business-card">
    <header class="brand">
      <span class="brand-dot" aria-hidden="true"></span>
      <div class="brand-text">
        <span class="brand-name">Bluebird Hosting</span>
        <span class="brand-tagline">Bright &amp; Fun-filled</span>
      </div>
    </header>

    <section class="name-band">
      <p class="person">Mack Dorran<span class="divider">|</span>Service Director</p>
    </section>

    <section class="contact">
      <div class="contact-row">
        <span class="contact-item">
          <span class="icon"><svg viewBox="0 0 12 12"><path d="M6 0.5a3.8 3.8 0 0 0-3.8 3.8C2.2 7 6 11.5 6 11.5S9.8 7 9.8 4.3A3.8 3.8 0 0 0 6 0.5zm0 5.3a1.5 1.5 0 1 1 0-3 1.5 1.5 0 0 1 0 3z"/></svg></span>
          Western Region
        </span>
        <span class="contact-item">
          <span class="icon"><svg viewBox="0 0 12 12"><path d="M2.6 0.8l1.8 2.3-1 1.3a7 7 0 0 0 4.2 4.2l1.3-1 2.3 1.8-1 2A9.6 9.6 0 0 1 0.6 1.8z"/></svg></span>
          877-555-0142
        </span>
        <span class="contact-item">
          <span class="icon"><svg viewBox="0 0 12 12"><path d="M2.6 0.8l1.8 2.3-1 1.3a7 7 0 0 0 4.2 4.2l1.3-1 2.3 1.8-1 2A9.6 9.6 0 0 1 0.6 1.8z"/></svg></span>
          801-555-0178
        </span>
        <span class="contact-item">
          <span class="icon"><svg viewBox="0 0 12 12"><path d="M2.6 0.8l1.8 2.3-1 1.3a7 7 0 0 0 4.2 4.2l1.3-1 2.3 1.8-1 2A9.6 9.6 0 0 1 0.6 1.8z"/></svg></span>
          1-801-555-0193
        </span>
      </div>
      <div class="contact-row">
        <span class="contact-item">
          <span class="icon"><svg viewBox="0 0 12 12"><path d="M1 2.5h10v7H1z M1.5 3l4.5 3.5L10.5 3" fill="none" stroke="#fff" stroke-width="1.1"/></svg></span>
          mack@mybluebirdhosting.com
        </span>
        <span class="contact-item">
          <span class="icon"><svg viewBox="0 0 12 12"><g fill="none" stroke="#fff" stroke-width="1"><circle cx="6" cy="6" r="4.8"/><ellipse cx="6" cy="6" rx="2" ry="4.8"/><path d="M1.2 6h9.6"/></g></svg></span>
          www.mybluebirdhosting.com
        </span>
      </div>
    </section>
  </main>
</body>
</html>
```